PROPERTY DEVELOPERS - LOGO & STATIONERY

We require a new logo design for a property development and sales company in Sydney, Australia.

We source land, build and sell residential & commercial investment properties including apartment buildings, townhouses, house and land packages in estates and retail shops.

We sell to local and overseas markets therefore the design needs to be a corporate effective global logo that would also suit the Asian market.

The company name is Corvane and we have been operating for 11 years and have been involved with over 5,000 properties. The focus should be on our company name Corvane with the word property as the word to explain ourselves.

This brief includes the logo design, business cards, letterhead, envelopes, with compliments slips and address label stickers.

We look forward to receiving exciting new designs.
All the best.

Reason: Designer who we were going to choose had their account closed.  Need some more options!

Property

Corvane Property

```html
<!DOCTYPE html>
<html lang="en">
<head>
<meta charset="utf-8">
<title>Corvane Property – Screen Identity</title>
<link rel="stylesheet" href="https://fonts.googleapis.com/css2?family=Lato:wght@300;400&display=swap">
<style>
  :root {
    --page: #ffffff;
    --dark-bg: #131313;
    --dark-name: #ffffff;
    --dark-rule: #6a6a6a;
    --dark-info: #5c5c5c;
    --light-bg-start: #ffffff;
    --light-bg-end: #e4e4e4;
    --light-name: #111111;
    --light-rule: #9a9a9a;
    --light-info: #8a8a8a;
    --mark: #7c7c7c;
    --divider: #b9b9b9;
  }
  * { margin: 0; padding: 0; box-sizing: border-box; }
  html, body { width: 900px; height: 1200px; overflow: hidden; background: var(--page); }
  body { font-family: "Lato", "Helvetica Neue", Arial, sans-serif; position: relative; }

  .screen {
    position: absolute;
    left: 40px;
    width: 820px;
    height: 500px;
    display: flex;
    flex-direction: column;
    align-items: center;
  }
  .screen--dark { top: 45px; background: var(--dark-bg); }
  .screen--light {
    top: 655px;
    background: linear-gradient(115deg, var(--light-bg-start) 0%, var(--light-bg-start) 38%, #f0f0f0 38.2%, var(--light-bg-end) 100%);
  }

  .divider {
    position: absolute;
    top: 600px;
    left: 0;
    width: 900px;
    border-top: 1px dashed var(--divider);
  }

  .brand {
    margin-top: 190px;
    display: flex;
    flex-direction: column;
    align-items: center;
  }
  .brand__mark {
    width: 14px;
    height: 14px;
    background: var(--mark);
    margin-bottom: 22px;
  }
  .brand__name {
    font-weight: 400;
    font-size: 56px;
    letter-spacing: 10px;
    line-height: 1;
    padding-left: 10px;
  }
  .brand__descriptor {
    font-weight: 400;
    font-size: 17px;
    letter-spacing: 9px;
    margin-top: 12px;
    padding-left: 9px;
  }
  .screen--dark .brand__name,
  .screen--dark .brand__descriptor { color: var(--dark-name); }
  .screen--light .brand__name,
  .screen--light .brand__descriptor { color: var(--light-name); }

  .contact {
    margin-top: 58px;
    width: 640px;
    padding-top: 16px;
    text-align: center;
    font-weight: 300;
    font-size: 13.5px;
    line-height: 19px;
    text-transform: uppercase;
  }
  .screen--dark .contact { border-top: 1px solid var(--dark-rule); color: var(--dark-info); }
  .screen--light .contact { border-top: 1px solid var(--light-rule); color: var(--light-info); }
  .contact__gap { display: inline-block; width: 10px; }
</style>
</head>
<body>

<section class="screen screen--dark">
  <div class="brand">
    <span class="brand__mark"></span>
    <span class="brand__name">CORVANE</span>
    <span class="brand__descriptor">PROPERTY</span>
  </div>
  <div class="contact">
    <p>Level 22, Tower Two Harbourline, 48 Merrow Street, Eastbrook NSW 2041</p>
    <p>T: 1300 555 010<span class="contact__gap"></span>E: info@corvaneproperty.com.au</p>
    <p>www.corvaneproperty.com.au</p>
  </div>
</section>

<div class="divider"></div>

<section class="screen screen--light">
  <div class="brand">
    <span class="brand__mark"></span>
    <span class="brand__name">CORVANE</span>
    <span class="brand__descriptor">PROPERTY</span>
  </div>
  <div class="contact">
    <p>Level 22, Tower Two Harbourline, 48 Merrow Street, Eastbrook NSW 2041</p>
    <p>T: 1300 555 010<span class="contact__gap"></span>E: info@corvaneproperty.com.au</p>
    <p>www.corvaneproperty.com.au</p>
  </div>
</section>

</body>
</html>
```